Business Card Trio Design

We need a set of business cards that all match but are not identical. We need one generic for the business and one for each of the two owners. We would like the cards to be similar to each other, but not identical. We have a logo and the colors of the logo are painstakingly chosen so if blue or green is used, we prefer our specific blue and green. Our logo pops better on a black background as well. We are open to double-sided, but it is not the top choice. We would love some either gold or silver accents that are in a foiled appearance. We sell uniforms (scrubs, culinary, EMT, police, fire, business, all types except kids and sports), shoes, equipment, and accessories. We also have quorvalink, mavelgrid, lumopixel, and yondrel that we would like to have them follow and we offer zembrix in the store we would like the card to also advertise.

```html
<!DOCTYPE html>
<html lang="en">
<head>
<meta charset="utf-8">
<title>Talvera Uniforms – Business Card</title>
<link rel="stylesheet" href="https://fonts.googleapis.com/css2?family=Cinzel:wght@600&family=Montserrat:wght@400;500&display=swap">
<style>
  :root {
    --brand-blue: #789fc0;
    --brand-green: #0e9470;
    --ink: #2a2a2a;
    --card-white: #f8f8f8;
    --backdrop: #dcdcdc;
    --faint-blue: #eaf0f3;
    --faint-green: #e0f0ec;
  }
  * { box-sizing: border-box; margin: 0; padding: 0; }
  html, body { width: 1200px; height: 900px; overflow: hidden; }
  body {
    background: var(--backdrop);
    font-family: "Montserrat", Arial, sans-serif;
    color: var(--ink);
    position: relative;
  }
  .card {
    position: absolute;
    left: 250px;
    width: 700px;
    height: 400px;
    border-radius: 26px;
    overflow: hidden;
    box-shadow: 0 6px 18px rgba(0,0,0,.18);
  }
  .card--back { top: 30px; background: var(--brand-blue); }
  .card--front { top: 470px; background: var(--card-white); }

  .brand { display: flex; align-items: center; gap: 18px; }
  .brand__dot { border-radius: 50%; flex: none; }
  .brand__name {
    font-family: "Cinzel", Georgia, serif;
    font-weight: 600;
    line-height: 1.05;
    letter-spacing: .06em;
    white-space: nowrap;
  }
  .card--back .brand {
    position: absolute; left: 50%; top: 50%;
    transform: translate(-50%, -50%);
  }
  .card--back .brand__dot { width: 96px; height: 96px; background: #fff; }
  .card--back .brand__name { color: #fff; font-size: 44px; }

  .front__decor {
    position: absolute; right: -40px; top: 20px;
    width: 360px; height: 300px; border-radius: 50%;
    background: linear-gradient(135deg, var(--faint-blue) 0%, var(--faint-blue) 55%, var(--faint-green) 100%);
  }
  .card--front .brand { position: absolute; left: 44px; top: 60px; }
  .card--front .brand__dot { width: 70px; height: 70px; background: var(--brand-green); }
  .card--front .brand__name { color: var(--brand-blue); font-size: 32px; }

  .person { position: absolute; left: 50px; top: 176px; }
  .person__name {
    font-family: "Cinzel", Georgia, serif; font-weight: 600;
    font-size: 28px; color: var(--brand-blue); letter-spacing: .03em;
    white-space: nowrap;
  }
  .person__name span { color: var(--brand-green); }
  .person__role { font-size: 17px; margin-top: 2px; }

  .contacts { position: absolute; left: 50px; top: 268px; list-style: none; }
  .contacts li { display: flex; align-items: center; gap: 12px; font-size: 17px; margin-bottom: 7px; white-space: nowrap; }
  .contacts svg { width: 16px; height: 16px; flex: none; }

  .divider {
    position: absolute; left: 420px; top: 262px;
    width: 2px; height: 90px; background: var(--brand-green);
  }
  .address { position: absolute; left: 442px; top: 262px; width: 240px; font-size: 15px; line-height: 1.45; }
  .social { display: flex; flex-wrap: nowrap; gap: 10px; margin-top: 8px; list-style: none; }
  .social li { font-size: 11px; font-weight: 500; color: var(--brand-green); white-space: nowrap; }
</style>
</head>
<body>
  <section class="card card--back" aria-label="Card back">
    <div class="brand">
      <span class="brand__dot"></span>
      <span class="brand__name">TALVERA<br>UNIFORMS</span>
    </div>
  </section>

  <section class="card card--front" aria-label="Card front">
    <div class="front__decor"></div>
    <div class="brand">
      <span class="brand__dot"></span>
      <span class="brand__name">TALVERA<br>UNIFORMS</span>
    </div>

    <div class="person">
      <p class="person__name">DORIN <span>VALCEK</span></p>
      <p class="person__role">Founder/CEO</p>
    </div>

    <ul class="contacts">
      <li>
        <svg viewBox="0 0 16 16"><path d="M4 1l3 3-1.5 2a8 8 0 004.5 4.5L12 9l3 3-2 2C7 14 2 9 2 3z" fill="var(--brand-green)"/></svg>
        555.014.2290
      </li>
      <li>
        <svg viewBox="0 0 16 16"><rect x="1" y="3" width="14" height="10" rx="1" fill="var(--brand-green)"/><path d="M1.5 4l6.5 5 6.5-5" stroke="#fff" stroke-width="1.3" fill="none"/></svg>
        hello@talverauniforms.com
      </li>
      <li>
        <svg viewBox="0 0 16 16" fill="none" stroke="var(--brand-green)" stroke-width="1.4"><circle cx="8" cy="8" r="6.5"/><ellipse cx="8" cy="8" rx="3" ry="6.5"/><path d="M1.5 8h13"/></svg>
        www.talverauniforms.com
      </li>
    </ul>

    <div class="divider"></div>
    <div class="address">
      <p>2146 Harlow Ave Suite 310<br>Brennick, AB 40718</p>
      <ul class="social">
        <li>quorvalink</li>
        <li>yondrel</li>
        <li>mavelgrid</li>
        <li>lumopixel</li>
      </ul>
    </div>
  </section>
</body>
</html>
```